Software company specialized in data analytics and professional services

We need a landing page design for our business. It should include our logo design. It should have multiple sections :
- stylish head
- what we do (data analytics software, professional services)
- contact form

Target Market(s)

Companies, B2B

Industry/Entity Type

Data

Number of Pages Required

1 page

Font styles to use
Sans Serif

Requirements
Must have
• Dark theme
Should not have
• Gradients on buttons

```html
<!DOCTYPE html>
<html lang="en">
<head>
<meta charset="utf-8">
<title>NovaMetric — Data Analytics &amp; Professional Services</title>
<link href="https://fonts.googleapis.com/css2?family=Bebas+Neue&family=Inter:wght@400;500;600;700&family=Poppins:wght@400;500;600&display=swap" rel="stylesheet">
<style>
  :root{
    --ink:#161616;
    --white:#ffffff;
    --violet:#8c0ff0;
    --violet-deep:#7a12e0;
    --blue:#1f86b8;
    --magenta:#e8108f;
    --text-dark:#2b2b33;
    --text-mute:#8a8fa3;
    --line:#e6e8ef;
    --navy:#3b3f8f;
    --green:#2fbf71;
    --red:#f0204a;
    --orange:#ff8a00;
  }
  *{box-sizing:border-box;margin:0;padding:0}
  html,body{width:1200px;height:2249px;overflow:hidden;background:var(--ink)}
  body{font-family:"Inter",sans-serif;color:var(--white)}
  .page{position:relative;width:1200px;height:2249px;overflow:hidden}
  .backdrop{position:absolute;left:0;top:0}
  .abs{position:absolute}

  .brand{font-family:"Inter",sans-serif;font-weight:700;color:var(--white);letter-spacing:1px}
  .brand--top{left:125px;top:32px;font-size:28px}
  .brand--foot{left:125px;top:2128px;font-size:52px;letter-spacing:2px}
  .copyright{right:125px;top:2151px;font-size:14px}

  .outline-title{font-family:"Bebas Neue",sans-serif;font-size:118px;line-height:1;color:transparent;-webkit-text-stroke:2px var(--white);letter-spacing:2px;white-space:nowrap}
  .solid-title{font-family:"Bebas Neue",sans-serif;color:var(--white);line-height:1;white-space:nowrap}
  .lead{font-size:15px;line-height:22px;color:var(--white)}

  .btn-contact{left:600px;top:456px;width:177px;height:40px;background:var(--magenta);color:var(--white);font-size:11px;font-weight:700;letter-spacing:3px;display:flex;align-items:center;justify-content:center;border:0}

  /* dashboard */
  .dash{left:-260px;top:115px;width:806px;height:573px;background:var(--white);border-radius:14px;font-family:"Poppins",sans-serif;color:var(--text-dark);overflow:hidden;box-shadow:0 10px 30px rgba(0,0,0,.15)}
  .dash .in{position:absolute}
  .dash__title{left:40px;top:72px;font-size:14px;font-weight:600;color:var(--navy)}
  .dash__head{right:22px;top:22px;display:flex;align-items:center;gap:14px;font-size:8px;color:var(--text-mute)}
  .dash__head b{color:var(--navy);font-weight:500}
  .ico-box{width:14px;height:12px;border:1.5px solid #666;border-radius:2px}
  .avatar{width:24px;height:24px;border-radius:50%;background:linear-gradient(135deg,#f3c1c8,#d86a7f)}
  .dash__select{left:667px;top:71px;width:123px;height:25px;border:1px solid var(--line);border-radius:5px;font-size:8px;color:var(--text-mute);display:flex;align-items:center;padding-left:8px}
  .dash__select b{color:var(--text-dark);font-weight:500;margin-left:3px}
  .stat{width:196px;height:87px;border:1px solid var(--line);border-radius:8px;padding:14px 14px}
  .stat__label{font-size:9px;color:var(--navy)}
  .stat__value{font-size:16px;font-weight:600;margin-top:6px}
  .stat__value small{font-size:8px;font-weight:400;margin-left:4px}
  .up{color:var(--green)} .down{color:var(--red)}
  .stat__sub{font-size:7.5px;color:var(--text-mute);margin-top:2px}
  .stat__icon{position:absolute;right:14px;top:14px;width:30px;height:30px;border-radius:7px}
  .panel{border:1px solid var(--line);border-radius:8px;height:246px;width:303px}
  .panel__title{position:absolute;left:14px;top:14px;font-size:10px;font-weight:600;color:var(--navy)}
  .table{position:absolute;left:14px;top:34px;width:275px;font-size:7.5px}
  .table__head{display:grid;grid-template-columns:1.3fr 1fr .8fr;background:#f3f4f8;height:14px;align-items:center;padding:0 12px;color:var(--text-mute);font-size:5.5px;letter-spacing:.3px}
  .table__row{display:grid;grid-template-columns:1.3fr 1fr .8fr;height:36px;align-items:center;padding:0 12px;border-bottom:1px solid #f0f1f5}
  .table__row span:last-child,.table__head span:last-child{text-align:right}
  .table__name{display:flex;align-items:center;gap:8px}
  .dot{width:14px;height:14px;border-radius:50%}

  /* small cards */
  .mini{background:var(--white);border-radius:8px;color:var(--text-dark);font-family:"Inter",sans-serif}
  .mini__label{position:absolute;font-weight:600}
  .mini__value{position:absolute;font-weight:700}

  /* services */
  .service{width:279px;height:302px;background:var(--white);color:var(--text-dark);text-align:center;padding:0 28px}
  .service__icon{margin:42px auto 0;display:block}
  .service__title{font-size:20px;font-weight:600;line-height:25px;margin-top:14px;color:#1e1e24}
  .service__text{font-size:12.5px;line-height:18px;margin-top:14px;color:#333}

  /* phone */
  .phone{left:771px;top:884px;width:245px;height:497px;background:var(--white);border:6px solid #eef0f4;border-radius:34px;overflow:hidden;color:#1e1e2a;font-family:"Poppins",sans-serif}
  .phone .in{position:absolute}
  .phone__title{left:12px;top:64px;font-size:25px;font-weight:500;line-height:29px;color:#14143a}
  .tabs{top:151px;left:10px;display:flex;gap:0;font-size:9px;color:var(--text-mute);align-items:center;white-space:nowrap}
  .tabs span{padding:3px 8px}
  .tabs .on{background:var(--red);color:var(--white);border-radius:10px;margin:0 10px}
  .tile{top:431px;height:40px;border-radius:4px;color:var(--white);font-size:11px;padding:5px 0 0 26px;line-height:13px}
  .tile small{display:block;font-size:7px;opacity:.85}

  /* contact */
  .form{left:125px;top:1516px;width:464px;height:448px;background:var(--white);color:#333}
  .form__title{position:absolute;top:64px;width:100%;text-align:center;font-size:18px;font-weight:600}
  .form__rule{position:absolute;left:176px;top:103px;width:113px;height:2px;background:var(--violet-deep)}
  .field{position:absolute;left:45px;width:374px;border:1px solid #cfcfd6;font-size:12px;color:#333;text-align:center;padding-top:10px}
  .send{position:absolute;left:212px;top:344px;width:40px;height:40px;border-radius:50%;background:var(--violet-deep);display:flex;align-items:center;justify-content:center}
  .contact-item{left:648px;display:flex;gap:14px;align-items:flex-start}
  .contact-item__icon{width:42px;height:42px;border-radius:50%;background:var(--white);display:flex;align-items:center;justify-content:center;flex:none}
  .contact-item h4{font-size:14px;font-weight:600;margin-top:2px}
  .contact-item p{font-size:12.5px;line-height:18px;margin-top:2px}
</style>
</head>
<body>
<div class="page">

  <svg class="backdrop" width="1200" height="2249" viewBox="0 0 1200 2249" aria-hidden="true">
    <defs>
      <linearGradient id="heroGrad" x1="0" y1="0" x2="1" y2="1">
        <stop offset="0" stop-color="#8c0ff0"/>
        <stop offset=".5" stop-color="#5a3ad8"/>
        <stop offset="1" stop-color="#1f86b8"/>
      </linearGradient>
      <linearGradient id="lowGrad" x1="1" y1="0" x2="0" y2="1">
        <stop offset="0" stop-color="#9210ec"/>
        <stop offset=".55" stop-color="#5c35d6"/>
        <stop offset="1" stop-color="#2a6fc6"/>
      </linearGradient>
    </defs>
    <rect width="1200" height="2249" fill="#161616"/>
    <polygon points="0,0 1200,0 1200,875 0,688" fill="url(#heroGrad)"/>
    <polygon points="0,1482 1200,1190 1200,2073 0,2073" fill="url(#lowGrad)"/>
  </svg>

  <!-- HERO -->
  <div class="abs brand brand--top">NOVAMETRIC</div>
  <div class="abs outline-title" style="left:346px;top:64px">CRAFTING SUCCESS</div>

  <div class="dash abs">
    <div class="in dash__head">
      <div class="ico-box"></div><div class="ico-box"></div>
      <span>Hi, <b>Rena</b></span>
      <div class="avatar" role="img" aria-label="User portrait"></div>
    </div>
    <div class="in dash__title">Dashboard</div>
    <div class="in dash__select">Show: <b>Weekly analytics</b> &nbsp;⌄</div>

    <div class="in stat" style="left:169px;top:105px"><div class="stat__label">Sessions</div><div class="stat__value">8,240<small class="up">(+12%)</small></div><div class="stat__sub">Analytics for last week</div><div class="stat__icon" style="background:#e6f1ff"></div></div>
    <div class="in stat" style="left:381px;top:105px"><div class="stat__label">Users</div><div class="stat__value">16,352<small class="up">(+21%)</small></div><div class="stat__sub">Analytics for last week</div><div class="stat__icon" style="background:#fde8ef"></div></div>
    <div class="in stat" style="left:593px;top:105px"><div class="stat__label">Time on Site</div><div class="stat__value">32m 12s<small class="up">(+50%)</small></div><div class="stat__sub">Analytics for last week</div><div class="stat__icon" style="background:#fff1e0"></div></div>
    <div class="in stat" style="left:169px;top:209px"><div class="stat__label">Pages</div><div class="stat__value">3,120<small class="up">(+8%)</small></div><div class="stat__sub">Analytics for last month</div><div class="stat__icon" style="background:#ecebff"></div></div>
    <div class="in stat" style="left:381px;top:209px"><div class="stat__label">Bounce Rate</div><div class="stat__value">56%<small class="down">(-14%)</small></div><div class="stat__sub">Analytics for last week</div><div class="stat__icon" style="background:#e3f7fb"></div></div>
    <div class="in stat" style="left:593px;top:209px"><div class="stat__label">New Sessions</div><div class="stat__value">94%<small class="up">(+50%)</small></div><div class="stat__sub">Analytics for last week</div><div class="stat__icon" style="background:#e3f8ee"></div></div>

    <div class="in panel" style="left:169px;top:311px">
      <div class="panel__title" style="left:14px">Device Share</div>
      <div class="in" style="left:14px;top:34px;width:270px;font-size:6.5px;line-height:11px;color:var(--text-mute)">Share of sessions by device type across all tracked channels this week, the rest come from other sources.</div>
      <svg class="in" style="left:88px;top:74px" width="126" height="126" viewBox="0 0 126 126">
        <circle cx="63" cy="63" r="52" fill="none" stroke="#ff9ccf" stroke-width="9" stroke-dasharray="190 400" transform="rotate(20 63 63)"/>
        <circle cx="63" cy="63" r="52" fill="none" stroke="#4aa8f5" stroke-width="9" stroke-dasharray="95 400" transform="rotate(140 63 63)"/>
        <circle cx="63" cy="63" r="52" fill="none" stroke="#4a4fc8" stroke-width="9" stroke-dasharray="40 400" transform="rotate(-88 63 63)"/>
      </svg>
      <div class="in" style="left:14px;top:222px;font-size:7.5px;display:flex;gap:26px;color:var(--text-dark)">
        <span>▣ Desktop (56%)</span><span style="color:#333"><b style="color:#4aa8f5">▣</b> Mobile (30%)</span><span><b style="color:#4a4fc8">▣</b> Tablet (14%)</span>
      </div>
    </div>

    <div class="in panel" style="left:487px;top:311px">
      <div class="panel__title">Browser Usage</div>
      <div class="table">
        <div class="table__head"><span>BROWSER</span><span>SESSIONS</span><span>BOUNCE RATE</span></div>
        <div class="table__row"><span class="table__name"><i class="dot" style="background:#f4b400"></i>Vantage</span><span>28,492</span><span>47.29%</span></div>
        <div class="table__row"><span class="table__name"><i class="dot" style="background:#2d9cf0"></i>Lumen</span><span>12,424</span><span>24.25%</span></div>
        <div class="table__row"><span class="table__name"><i class="dot" style="background:#e3242b"></i>Orbit</span><span>17,283</span><span>41.48%</span></div>
        <div class="table__row"><span class="table__name"><i class="dot" style="background:#ff8a2a"></i>Ember</span><span>25,382</span><span>44.32%</span></div>
        <div class="table__row"><span class="table__name"><i class="dot" style="background:#1ba1e2"></i>Drift</span><span>46,382</span><span>76.39%</span></div>
      </div>
    </div>
  </div>

  <div class="abs solid-title" style="left:600px;top:196px;font-size:72px;line-height:70px">STORIES THROUGH<br>ADVANCED ANALYTICS</div>
  <p class="abs lead" style="left:600px;top:361px;width:400px">Lorem Ipsum is simply dummy text of the printing and typesetting industry. Lorem Ipsum has been the industry's standard dummy text ever since the 1500s,</p>
  <button class="abs btn-contact">CONTACT US</button>

  <svg class="abs" style="left:863px;top:549px" width="146" height="146" aria-hidden="true">
    <defs><pattern id="dots" width="17" height="17" patternUnits="userSpaceOnUse"><rect x="1" y="1" width="4" height="4" fill="#ffffff" opacity=".75"/></pattern></defs>
    <rect width="146" height="146" fill="url(#dots)"/>
  </svg>

  <div class="abs mini" style="left:956px;top:474px;width:231px;height:156px">
    <div class="mini__label" style="left:21px;top:21px;font-size:15.5px">GROSS SALES</div>
    <div class="mini__value" style="left:21px;top:42px;font-size:15px;color:#1f6fa8">$2300</div>
    <svg class="abs" style="left:190px;top:26px" width="22" height="22" viewBox="0 0 22 22"><path d="M3 17 L9 10 L13 14 L19 5" fill="none" stroke="#e8108f" stroke-width="2"/></svg>
    <svg class="abs" style="left:21px;top:70px" width="190" height="70" viewBox="0 0 190 70">
      <defs><linearGradient id="gs" x1="0" y1="0" x2="0" y2="1"><stop offset="0" stop-color="#6b7ff0" stop-opacity=".55"/><stop offset="1" stop-color="#ffffff" stop-opacity="0"/></linearGradient></defs>
      <path d="M0 30 C15 5 30 5 45 30 S75 55 90 30 S120 5 135 30 S165 55 190 30 V70 H0Z" fill="url(#gs)"/>
      <path d="M0 30 C15 5 30 5 45 30 S75 55 90 30 S120 5 135 30 S165 55 190 30" fill="none" stroke="#4a5fe0" stroke-width="2"/>
    </svg>
  </div>

  <div class="abs mini" style="left:734px;top:592px;width:192px;height:128px">
    <div class="mini__label" style="left:18px;top:15px;font-size:13px">NET SALES</div>
    <div class="mini__value" style="left:18px;top:33px;font-size:13px;color:#8c0ff0">$2300</div>
    <svg class="abs" style="left:152px;top:18px" width="20" height="20" viewBox="0 0 20 20"><path d="M2 15 L8 9 L12 13 L18 4" fill="none" stroke="#1f86b8" stroke-width="2"/></svg>
    <svg class="abs" style="left:18px;top:55px" width="158" height="64" viewBox="0 0 158 64">
      <defs><linearGradient id="ns" x1="0" y1="0" x2="0" y2="1"><stop offset="0" stop-color="#f04aa8" stop-opacity=".5"/><stop offset="1" stop-color="#ffffff" stop-opacity="0"/></linearGradient></defs>
      <path d="M0 22 C12 42 26 42 38 22 S64 2 79 22 S104 42 118 22 S146 2 158 22 V64 H0Z" fill="url(#ns)"/>
      <path d="M0 22 C12 42 26 42 38 22 S64 2 79 22 S104 42 118 22 S146 2 158 22" fill="none" stroke="#e0208f" stroke-width="2"/>
    </svg>
  </div>

  <!-- WHAT WE DO -->
  <div class="abs outline-title" style="left:253px;top:818px">TRANSFORMING</div>
  <div class="abs solid-title" style="right:489px;top:932px;font-size:60px;line-height:58px;text-align:right">DATA INTO ACTIONABLE<br>INTELLIGENCE</div>

  <article class="abs service" style="left:132px;top:1074px">
    <svg class="service__icon" width="44" height="44" viewBox="0 0 44 44" aria-hidden="true">
      <rect x="3" y="4" width="38" height="28" rx="2" fill="none" stroke="#b012d8" stroke-width="3"/>
      <rect x="10" y="16" width="4" height="12" fill="#b012d8"/><rect x="17" y="11" width="4" height="17" fill="#b012d8"/><rect x="24" y="19" width="4" height="9" fill="#b012d8"/>
      <circle cx="33" cy="15" r="4" fill="#b012d8"/>
      <rect x="19" y="32" width="6" height="5" fill="#b012d8"/><rect x="12" y="37" width="20" height="3" fill="#b012d8"/>
    </svg>
    <h3 class="service__title">DATA ANALYTICS</h3>
    <p class="service__text">Lorem Ipsum is simply dummy text of the printing and typesetting industry. Lorem Ipsum has been the industry's standard dummy text ever since the 1500s,</p>
  </article>

  <article class="abs service" style="left:432px;top:1074px">
    <svg class="service__icon" width="50" height="50" viewBox="0 0 50 50" aria-hidden="true" style="margin-top:36px">
      <circle cx="14" cy="8" r="5" fill="#b012d8"/><circle cx="25" cy="8" r="5" fill="#b012d8"/><circle cx="36" cy="8" r="5" fill="#b012d8"/>
      <rect x="7" y="15" width="36" height="8" rx="4" fill="#b012d8"/>
      <circle cx="25" cy="32" r="10" fill="none" stroke="#b012d8" stroke-width="4"/>
      <path d="M5 30 L12 36 L5 42 Z M45 30 L38 36 L45 42 Z" fill="#b012d8"/>
      <rect x="15" y="44" width="20" height="5" rx="2" fill="#b012d8"/>
    </svg>
    <h3 class="service__title">PROFESSIONAL<br>SERVICES</h3>
    <p class="service__text">Lorem Ipsum is simply dummy text of the printing and typesetting industry. Lorem Ipsum has been the industry's standard dummy text ever since the 1500s,</p>
  </article>

  <div class="phone abs">
    <div class="in" style="left:60px;top:0;width:120px;height:18px;background:#eef0f4;border-radius:0 0 12px 12px"></div>
    <div class="in" style="left:10px;top:36px;width:10px;height:8px;border-top:2px solid #333;border-bottom:2px solid #333"></div>
    <div class="in phone__title">Summary<br>Report</div>
    <div class="in avatar" role="img" aria-label="Profile portrait" style="left:200px;top:76px;width:26px;height:26px;background:linear-gradient(135deg,#d9d2cc,#7d6a60)"></div>
    <div class="in tabs"><span>1 month</span><span class="on">3 month</span><span>6 month</span><span>1 year</span></div>
    <svg class="in" style="left:0;top:190px" width="240" height="200" viewBox="0 0 240 200">
      <g stroke="#eceef3" stroke-width="1">
        <line x1="30" y1="0" x2="30" y2="180"/><line x1="60" y1="0" x2="60" y2="180"/><line x1="90" y1="0" x2="90" y2="180"/><line x1="120" y1="0" x2="120" y2="180"/><line x1="150" y1="0" x2="150" y2="180"/><line x1="210" y1="0" x2="210" y2="180"/>
      </g>
      <line x1="178" y1="20" x2="178" y2="180" stroke="#9aa0b4" stroke-dasharray="3 3"/>
      <path d="M0 80 C15 20 25 15 40 35 S70 60 85 75 S110 120 125 90 S150 85 165 95 S190 115 200 105 S225 100 240 110" fill="none" stroke="#3447c8" stroke-width="1.5"/>
      <path d="M0 115 C20 125 35 115 50 120 S65 100 75 110 S95 110 105 90 S120 60 135 70 S160 90 178 102 S195 60 205 55 S225 70 240 80" fill="none" stroke="#f0204a" stroke-width="1.5"/>
      <circle cx="178" cy="102" r="3" fill="#fff" stroke="#f0204a" stroke-width="1.5"/>
      <rect x="148" y="55" width="62" height="20" rx="3" fill="#14143a"/>
      <text x="179" y="69" fill="#fff" font-size="9" font-family="Poppins,sans-serif" text-anchor="middle">1:25:22</text>
      <g fill="#9aa0b4" font-size="7" font-family="Poppins,sans-serif">
        <text x="8" y="198">11/8</text><text x="34" y="198">11/9</text><text x="58" y="198">11/10</text><text x="86" y="198">11/11</text><text x="114" y="198">11/12</text><text x="143" y="198">11/13</text><text x="172" y="198">11/14</text>
      </g>
    </svg>
    <div class="in tile" style="left:8px;width:74px;background:var(--red)">36 138<small>Steps</small></div>
    <div class="in tile" style="left:90px;width:78px;background:#5b5fe0">20,4 h<small>Swimming</small></div>
    <div class="in tile" style="left:176px;width:70px;background:var(--orange)">20<small>km</small></div>
  </div>

  <!-- CONTACT -->
  <div class="abs outline-title" style="left:527px;top:1478px">YOUR DATA</div>
  <div class="abs solid-title" style="left:649px;top:1592px;font-size:58px">OUR EXPERTISE</div>
  <p class="abs" style="left:649px;top:1671px;width:400px;font-size:12.5px;line-height:18px">Lorem Ipsum is simply dummy text of the printing and typesetting industry. Lorem Ipsum has been the industry's standard dummy text ever since the 1500s,</p>

  <div class="abs contact-item" style="top:1751px">
    <span class="contact-item__icon"><svg width="18" height="18" viewBox="0 0 24 24"><path d="M6 3 L10 3 L11 8 L8.5 9.5 C10 12.5 11.5 14 14.5 15.5 L16 13 L21 14 L21 18 C21 19.5 20 20.5 18.5 20.5 C10 20 4 14 3.5 5.5 C3.5 4 4.5 3 6 3Z" fill="#7a12e0"/></svg></span>
    <div><h4>Call Now</h4><p>123-456-7890</p></div>
  </div>
  <div class="abs contact-item" style="top:1824px">
    <span class="contact-item__icon"><svg width="18" height="14" viewBox="0 0 18 14"><rect width="18" height="14" rx="2" fill="#7a12e0"/><path d="M1 2 L9 8 L17 2" fill="none" stroke="#fff" stroke-width="1.5"/></svg></span>
    <div><h4>Email Us</h4><p>info@novametric.com</p></div>
  </div>
  <div class="abs contact-item" style="top:1898px">
    <span class="contact-item__icon"><svg width="16" height="20" viewBox="0 0 16 20"><path d="M8 0 C3.6 0 0 3.4 0 7.6 C0 13 8 20 8 20 C8 20 16 13 16 7.6 C16 3.4 12.4 0 8 0Z" fill="#7a12e0"/><circle cx="8" cy="7.5" r="3" fill="#fff"/></svg></span>
    <div><h4>Address</h4><p>Lorem ipsum is a<br>dummy text</p></div>
  </div>

  <form class="abs form">
    <h2 class="form__title">GET IN TOUCH WITH US</h2>
    <div class="form__rule"></div>
    <div class="field" style="top:131px;height:36px">Name</div>
    <div class="field" style="top:176px;height:37px">Email</div>
    <div class="field" style="top:223px;height:141px">Message</div>
    <span class="send"><svg width="18" height="18" viewBox="0 0 24 24"><path d="M2 11 L22 2 L15 22 L11 13 Z" fill="#fff"/><path d="M11 13 L22 2" stroke="#7a12e0" stroke-width="1.5"/></svg></span>
  </form>

  <!-- FOOTER -->
  <div class="abs brand brand--foot">NOVAMETRIC</div>
  <div class="abs copyright">© 2023-NovaMetric</div>
</div>
</body>
</html>
```